Stationery Design Project

Our company is "Meridal Systems" and we have a product called "quillbrook.com". The product is an online accounting software for businesses. We want to communicate that our software will help business owners to be more efficient and help them track their finances better. Quillbrook.com is basically a simple version of ledgerpine.

"We want a unique and creative design which will surprise our customer."

NAME CARD = QUILLBROOK
We want a quillbrook name card NOT MERIDAL SYSTEMS.

For the content of the name card, please make sure it fit with a long name like the following:

Roswin Halim Alias Roswin
Developer Specialist
T: (021) 4172 3846
F: (021) 4172 3847
E: customer.service@mrd.co.id

I need you to put it the following information to the name card

"quillbrook"
- moto is "automate your businesses"
- website "www.quillbrook.com"
- quillbrook is a "Web Accounting Software"
- product of "Meridal Systems"

LETTERHEAD, ENVELOPE, FOLDER = MERIDAL SYSTEMS
Other than name card we wanted you to design for us; letterhead, envelope and folder. In letterhead, envelope and folder it should ONLY contain the following information ("Meridal Systems").
PLEASE BE SURE YOU ARE NOT PUTTING "QUILLBROOK LOGO" IN LETTERHEAD, ENVELOPE AND FOLDER.

"Meridal Systems"
Address:
Ruko Harbor Plaza Blok. D No. 18
Jl. Kembangsari No. 47
Jakarta
Kalideres, 11840
Indonesia

Web Address: mrd.co.id

T: (021) 4172 3846
F: (021) 4172 3847

Target Market(s)

Business Owners, Accountant, Auditor, Tax Consultant

Industry/Entity Type

Accounting

Requirements
Must have
• .

```html
<!DOCTYPE html>
<html lang="en">
<head>
<meta charset="utf-8">
<title>Meridal Systems Stationery</title>
<link href="https://fonts.googleapis.com/css2?family=Pathway+Gothic+One&display=swap" rel="stylesheet">
<style>
  :root{
    --stage:#5a5a5b;
    --black:#050505;
    --green-dark:#1d4a1c;
    --green:#4f8a23;
    --lime:#c9d400;
    --paper:#ffffff;
    --paper-grey:#e3e3e3;
    --ink-grey:#6a6a6a;
    --ink-light:#d8d8d8;
    --navy:#1a2a6c;
    --mark-blue:#2d6fb0;
  }
  *{box-sizing:border-box;margin:0;padding:0}
  html,body{width:1200px;height:950px;overflow:hidden;background:var(--stage)}
  body{position:relative;font-family:"Pathway Gothic One",sans-serif;letter-spacing:.04em}
  .piece{position:absolute;overflow:hidden}
  .accent-line{position:absolute;left:0;right:0;background:linear-gradient(90deg,var(--green-dark),var(--green) 25%,var(--lime) 50%,var(--green) 75%,var(--green-dark))}
  .brand{display:flex;align-items:center;gap:6px;white-space:nowrap}
  .brand-dot{border-radius:50%;background:var(--mark-blue);flex:none}
  .brand-name{color:var(--ink-light)}

  /* card front */
  .card-front{left:121px;top:29px;width:219px;height:144px;border-radius:7px;background:radial-gradient(ellipse at 50% 75%,#7bb32e,#3e7a1e 55%,#163814);}
  .card-front .top-strip{position:absolute;left:0;right:0;top:0;height:9px;background:linear-gradient(90deg,#2c5c1a,#8fbf2c,#2c5c1a)}
  .card-front .black-band{position:absolute;left:0;right:0;top:9px;height:59px;background:var(--black);display:flex;flex-direction:column;align-items:center;padding-top:10px}
  .card-front .brand-name{font-size:15px}
  .card-front .tagline{margin-top:4px;font-size:8px;line-height:10px;color:var(--ink-light);text-align:left;width:70px;margin-left:30px}
  .product-box{position:absolute;left:69px;top:77px;width:121px;height:31px;background:var(--black);border:1px solid #ccc;color:#fff;font-size:20px;display:flex;align-items:center;justify-content:center}
  .card-front .product-lines{position:absolute;left:71px;top:111px;font-size:6.5px;line-height:8.5px;color:#e8f0c0}

  /* card back */
  .card-back{left:357px;top:29px;width:219px;height:144px;border-radius:7px;background:linear-gradient(180deg,#fafafa,#f2f2f2 60%,#d0d0d0 88%)}
  .card-back .black-band{position:absolute;left:0;right:0;top:0;height:34px;background:var(--black);display:flex;align-items:center;justify-content:space-between;padding:0 10px}
  .card-back .brand-name{font-size:12px}
  .card-back .product-name{color:#fff;font-size:17px}
  .card-back .person{position:absolute;left:9px;top:47px}
  .person-name{color:var(--navy);font-size:13px;font-weight:400}
  .person-role{color:#777;font-size:10px;margin-top:1px}
  .card-back .contact{position:absolute;left:9px;top:87px;font-size:7.5px;line-height:10px;color:#777}
  .email{color:var(--navy)}
  .card-back .foot{position:absolute;left:0;right:0;bottom:0;height:12px;background:#0f2c12}

  /* letterhead */
  .letterhead{left:85px;top:210px;width:510px;height:720px;background:var(--paper)}
  .letterhead .brand{position:absolute;left:16px;top:36px;gap:10px}
  .letterhead .brand-dot{width:42px;height:42px}
  .letterhead .brand-name{color:#5a5a5a;font-size:26px}
  .letterhead .footer{position:absolute;left:0;right:0;bottom:0;height:72px;background:var(--black)}
  .address,.phones{position:absolute;font-size:8.5px;line-height:10.3px;color:#cfcfcf}
  .letterhead .address{left:15px;top:13px}
  .letterhead .phones{left:170px;top:13px}
  .letterhead .footer .brand-dot{position:absolute;right:32px;top:14px;width:46px;height:46px}

  /* envelope front */
  .envelope-front{left:610px;top:190px;width:534px;height:267px;background:linear-gradient(180deg,#dcdcdc 0,#efefef 8%,#ffffff 35%,#f2f2f2 70%,#c8c8c8 100%)}
  .envelope-front .band{position:absolute;left:0;right:0;top:21px;height:56px;background:var(--black)}
  .envelope-front .brand{position:absolute;left:22px;top:8px;gap:10px}
  .envelope-front .brand-dot{width:40px;height:40px}
  .envelope-front .brand-name{font-size:22px}
  .envelope-front .address,.envelope-front .phones{color:#777;top:197px}
  .envelope-front .address{left:21px}
  .envelope-front .phones{left:162px}
  .envelope-front .phones .email,.envelope-front .phones .web{color:var(--navy)}

  /* envelope back */
  .envelope-back{left:616px;top:486px;width:534px;height:267px;background:linear-gradient(180deg,#ffffff 0,#f4f4f4 45%,#ffffff 60%,#c8c8c8 100%)}
  .flap{position:absolute;left:0;top:0;width:534px;height:66px}
  .envelope-back .brand{position:absolute;left:0;right:0;top:8px;flex-direction:column;gap:3px}
  .envelope-back .brand-dot{width:34px;height:34px}
  .envelope-back .brand-name{font-size:11px}
</style>
</head>
<body>

<section class="piece card-front" aria-label="Quillbrook name card, front">
  <div class="top-strip"></div>
  <div class="black-band">
    <div class="brand"><span class="brand-dot" style="width:18px;height:18px"></span><span class="brand-name">MERIDAL SYSTEMS</span></div>
    <p class="tagline">DIGITIZE LIFE<br>MRD.CO.ID</p>
  </div>
  <div class="product-box">quillbrook</div>
  <p class="product-lines">AUTOMATE YOUR BUSINESSES<br>WWW.QUILLBROOK.COM<br>WEB ACCOUNTING SOFTWARE</p>
</section>

<section class="piece card-back" aria-label="Quillbrook name card, back">
  <div class="black-band">
    <div class="brand"><span class="brand-dot" style="width:16px;height:16px"></span><span class="brand-name">MERIDAL SYSTEMS</span></div>
    <span class="product-name">quillbrook</span>
  </div>
  <div class="accent-line" style="top:34px;height:3px"></div>
  <div class="person">
    <p class="person-name">ROSWIN HALIM ALIAS ROSWIN</p>
    <p class="person-role">DEVELOPER SPECIALIST</p>
  </div>
  <p class="contact">T: (021) 4172 3846<br>F: (021) 4172 3847<br><span class="email">E: CUSTOMER.SERVICE@MRD.CO.ID</span></p>
  <div class="accent-line" style="bottom:12px;height:6px"></div>
  <div class="foot"></div>
</section>

<section class="piece letterhead" aria-label="Meridal Systems letterhead">
  <div class="brand"><span class="brand-dot"></span><span class="brand-name">MERIDAL SYSTEMS</span></div>
  <div class="accent-line" style="bottom:72px;height:5px"></div>
  <div class="footer">
    <p class="address">RUKO HARBOR PLAZA BLOK. D NO. 18<br>JL. KEMBANGSARI NO. 47<br>JAKARTA<br>KALIDERES, 11840<br>INDONESIA</p>
    <p class="phones">T: (021) 4172 3846<br>F: (021) 4172 3847<br>E: CUSTOMER.SERVICE@MRD.CO.ID<br>W: MRD.CO.ID</p>
    <span class="brand-dot"></span>
  </div>
</section>

<section class="piece envelope-front" aria-label="Meridal Systems envelope, front">
  <div class="band">
    <div class="brand"><span class="brand-dot"></span><span class="brand-name">MERIDAL SYSTEMS</span></div>
  </div>
  <div class="accent-line" style="top:77px;height:3px"></div>
  <p class="address">RUKO HARBOR PLAZA BLOK. D NO. 18<br>JL. KEMBANGSARI NO. 47<br>JAKARTA<br>KALIDERES, 11840<br>INDONESIA</p>
  <p class="phones">T: (021) 4172 3846<br>F: (021) 4172 3847<br><span class="email">E: CUSTOMER.SERVICE@MRD.CO.ID</span><br><span class="web">W: MRD.CO.ID</span></p>
  <div class="accent-line" style="bottom:0;height:5px"></div>
</section>

<section class="piece envelope-back" aria-label="Meridal Systems envelope, back">
  <svg class="flap" viewBox="0 0 534 66" aria-hidden="true">
    <polygon points="0,0 534,0 498,66 30,66" fill="#050505"/>
  </svg>
  <div class="brand"><span class="brand-dot"></span><span class="brand-name">MERIDAL SYSTEMS</span></div>
  <div class="accent-line" style="bottom:0;height:7px"></div>
</section>

</body>
</html>
```